ashby paving works

Needs to have phone number 0412885107 and email marklowry@pavemail.com.au.
ABN 27613048852
name mark lowry

For all your concreting solutions
Excavation
Exposed & colour concrete
House & shed slabs
Driveways
Landing & steps

Contact Information for Business Card

ph 0412885107
email marklowry@pavemail.com.au.
ABN 27613048852
name mark lowry

```html
<!DOCTYPE html>
<html lang="en">
<head>
<meta charset="utf-8">
<title>Ashby Paving Works – Business Card</title>
<link href="https://fonts.googleapis.com/css2?family=Lato:wght@400;700&display=swap" rel="stylesheet">
<style>
  :root {
    --backdrop: #3b322d;
    --card: #1c1c1d;
    --orange: #f26a21;
    --grey: #8a8a8a;
    --white: #f2f2f2;
  }
  * { margin: 0; padding: 0; box-sizing: border-box; }
  html, body { width: 1200px; height: 715px; overflow: hidden; }
  body {
    background: var(--backdrop);
    font-family: "Lato", Arial, sans-serif;
    position: relative;
  }
  .card {
    position: absolute;
    top: 206px;
    width: 530px;
    height: 303px;
    background: var(--card);
    overflow: hidden;
  }
  .card--front { left: 50px; }
  .card--back { left: 620px; }

  /* brand lockup */
  .brand { position: absolute; display: flex; align-items: center; }
  .brand__mark { background: var(--orange); flex: none; }
  .brand__rule { width: 1px; background: var(--orange); flex: none; }
  .brand__text { display: flex; flex-direction: column; align-items: center; }
  .brand__name {
    color: var(--orange); font-weight: 700; text-transform: uppercase;
    white-space: nowrap; letter-spacing: 0.02em;
  }
  .brand__divider { height: 1px; background: var(--grey); width: 100%; }
  .brand__phone { color: var(--orange); letter-spacing: 0.12em; }

  .card--front .brand { left: 122px; top: 104px; gap: 16px; }
  .card--front .brand__mark { width: 48px; height: 48px; }
  .card--front .brand__rule { height: 78px; transform: rotate(14deg); }
  .card--front .brand__name { font-size: 21px; }
  .card--front .brand__divider { margin: 6px 0 5px; }
  .card--front .brand__phone { font-size: 14px; }

  .card--back .brand { left: 34px; top: 30px; gap: 10px; }
  .card--back .brand__mark { width: 30px; height: 30px; }
  .card--back .brand__rule { height: 48px; transform: rotate(14deg); }
  .card--back .brand__name { font-size: 13px; }
  .card--back .brand__divider { margin: 4px 0 3px; }
  .card--back .brand__phone { font-size: 9px; }

  .accent-line {
    position: absolute; left: 70px; top: 120px;
    width: 400px; height: 1.5px; background: var(--orange);
  }
  .contact { position: absolute; left: 42px; top: 150px; list-style: none; }
  .contact__item {
    display: flex; align-items: center; gap: 8px;
    color: var(--white); font-size: 14px; line-height: 20px;
  }
  .contact__icon { width: 10px; height: 10px; flex: none; }

  .person { position: absolute; right: 34px; top: 164px; text-align: right; }
  .person__name {
    color: var(--orange); font-size: 25px; font-weight: 700;
    letter-spacing: 0.02em; text-transform: uppercase; line-height: 1;
  }
  .person__role { color: var(--white); font-size: 14px; margin-top: 3px; }
  .business-number { position: absolute; right: 34px; top: 220px; text-align: right; font-size: 14px; line-height: 17px; }
  .business-number__label { color: var(--orange); }
  .business-number__value { color: var(--white); }
  .website {
    position: absolute; left: 250px; top: 258px;
    color: var(--white); font-size: 14px;
  }
  .website__domain { color: var(--orange); }

  .stripe { position: absolute; }
  .stripe--grey { left: 0; top: 256px; width: 236px; height: 3px; background: var(--grey); }
  .stripe--orange { left: 0; top: 284px; width: 420px; height: 8px; background: var(--orange); }
  .stripe--grey-end { left: 420px; top: 286px; width: 110px; height: 3px; background: var(--grey); }
</style>
</head>
<body>
  <section class="card card--front">
    <div class="brand">
      <span class="brand__mark"></span>
      <span class="brand__rule"></span>
      <div class="brand__text">
        <span class="brand__name">Ashby Paving Works</span>
        <span class="brand__divider"></span>
        <span class="brand__phone">0412885107</span>
      </div>
    </div>
  </section>

  <section class="card card--back">
    <div class="brand">
      <span class="brand__mark"></span>
      <span class="brand__rule"></span>
      <div class="brand__text">
        <span class="brand__name">Ashby Paving Works</span>
        <span class="brand__divider"></span>
        <span class="brand__phone">0412885107</span>
      </div>
    </div>

    <span class="accent-line"></span>

    <ul class="contact">
      <li class="contact__item">
        <svg class="contact__icon" viewBox="0 0 10 10"><path d="M2 1 L4 1 L4.6 3 L3.4 3.8 Q4.4 5.8 6.2 6.6 L7 5.4 L9 6 L9 8 Q8.4 9 7 9 Q1 7.4 1 2.4 Q1 1 2 1 Z" fill="#f26a21"/></svg>
        +61 412 885 107
      </li>
      <li class="contact__item">
        <svg class="contact__icon" viewBox="0 0 10 10"><rect x="0.8" y="2" width="8.4" height="6" fill="none" stroke="#f26a21" stroke-width="1"/><path d="M1 2.4 L5 5.4 L9 2.4" fill="none" stroke="#f26a21" stroke-width="1"/></svg>
        marklowry@pavemail.com.au
      </li>
    </ul>

    <div class="person">
      <p class="person__name">Mark Lowry</p>
      <p class="person__role">Director</p>
    </div>

    <div class="business-number">
      <p class="business-number__label">ABN</p>
      <p class="business-number__value">27613048852</p>
    </div>

    <p class="website">www.<span class="website__domain">ashbypaving</span>.com.au</p>

    <span class="stripe stripe--grey"></span>
    <span class="stripe stripe--orange"></span>
    <span class="stripe stripe--grey-end"></span>
  </section>
</body>
</html>
```